Catalogue design for construction materials supplies

We need to design a new product catalogue for building material supply company based in Singapore called "Tembusu Harbour Supplies Pte Ltd" . We supply a wide range of construction related materials in the local market and is one of the leading stockist of construction material in Singapore. We would like the design to be modern and industrial showing green sustainable building.
Updates

Reason: I would not be able to consolidate for my supervisor to decide on the design as I will be away for business trip the next 4 days. My Apologies.

Target Market(s)

Developers, Main Constructors, Sub Contractors, Construction company

Industry/Entity Type

Construction

Font styles to use
Serif

Colors
0255a3
ffc214
ec1f27
85acd3
abd037
9bcb3b
3276b5
fbed22
f37122

Requirements
Must have
• Company Logo, awards logo, product pictures

```html
<!DOCTYPE html>
<html lang="en">
<head>
<meta charset="utf-8">
<title>Construction Material Catalogue 2016 – Tembusu Harbour Supplies Pte Ltd</title>
<link rel="stylesheet" href="https://fonts.googleapis.com/css2?family=Anton&family=Oswald:wght@600&family=Noto+Serif+SC:wght@700&display=swap">
<style>
  :root {
    --canvas: #e8e9ea;
    --band-green: #9bcb3b;
    --stripe-green: #abd037;
    --stripe-yellow: #ffc214;
    --brand-red: #ec1f27;
    --brand-navy: #1f3f95;
    --title-dark: #3a3a3c;
    --title-blue: #0a59a8;
    --title-orange: #f37122;
    --photo-light: #c9ccce;
    --photo-dark: #6f7477;
    --haze-light: #eef0f1;
    --haze-mid: #d9dcdf;
  }
  html, body {
    margin: 0;
    padding: 0;
    overflow: hidden;
    background: var(--canvas);
  }
  .cover {
    width: 848px;
    height: 1200px;
    overflow: hidden;
    background: var(--canvas);
  }
  .cover svg { display: block; width: 848px; height: 1200px; }
  .brand-name-cn { font-family: "Noto Serif SC", serif; font-weight: 700; fill: var(--brand-red); }
  .brand-name-en { font-family: "Oswald", sans-serif; font-weight: 600; fill: var(--brand-navy); }
  .title { font-family: "Anton", sans-serif; }
  .title-construction { fill: var(--title-dark); }
  .title-material { fill: var(--title-blue); }
  .title-catalogue { fill: var(--title-orange); }
  .title-year { fill: var(--title-dark); }
</style>
</head>
<body>
<main class="cover">
  <svg viewBox="0 0 919 1300" preserveAspectRatio="none" xmlns="http://www.w3.org/2000/svg">
    <defs>
      <linearGradient id="photoTone" x1="0" y1="0" x2="1" y2="1">
        <stop offset="0" stop-color="var(--photo-dark)"/>
        <stop offset="0.5" stop-color="var(--photo-light)"/>
        <stop offset="1" stop-color="var(--photo-dark)"/>
      </linearGradient>
      <linearGradient id="hazeTone" x1="0" y1="0" x2="1" y2="1">
        <stop offset="0" stop-color="var(--haze-mid)"/>
        <stop offset="1" stop-color="var(--haze-light)"/>
      </linearGradient>
    </defs>

    <rect class="top-band" x="0" y="0" width="919" height="28" fill="var(--band-green)"/>
    <rect class="top-rule" x="0" y="28" width="919" height="8" fill="var(--brand-red)"/>

    <g role="img" aria-label="Faded photo of a worker laying aerated concrete blocks">
      <rect x="0" y="660" width="919" height="640" fill="url(#hazeTone)"/>
    </g>

    <polygon class="stripe-green" points="705,36 770,36 700,205 638,205" fill="var(--stripe-green)"/>
    <polygon class="stripe-yellow" points="805,36 890,36 825,205 760,205" fill="var(--stripe-yellow)"/>

    <polygon class="frame-left" points="0,165 215,165 0,720" fill="var(--brand-red)"/>
    <polygon class="frame-right" points="919,150 919,700 705,700" fill="var(--brand-red)"/>

    <g role="img" aria-label="Photo of a worker in red gloves aligning a large aerated concrete block on site">
      <polygon points="178,205 868,205 770,660 30,660" fill="url(#photoTone)"/>
    </g>

    <polygon class="stripe-green" points="530,660 585,660 548,740 492,740" fill="var(--stripe-green)"/>
    <polygon class="stripe-yellow" points="622,660 702,660 662,740 598,740" fill="var(--stripe-yellow)"/>

    <g class="brand">
      <rect class="brand-mark" x="33" y="56" width="75" height="75" fill="var(--brand-red)"/>
      <text class="brand-name-cn" x="120" y="92" font-size="24" textLength="365" lengthAdjust="spacing">淡布苏港供应私人有限公司</text>
      <text class="brand-name-en" x="120" y="127" font-size="27" textLength="370" lengthAdjust="spacingAndGlyphs">TEMBUSU HARBOUR SUPPLIES PTE LTD</text>
    </g>

    <rect class="title-bar" x="605" y="843" width="314" height="85" fill="var(--title-blue)"/>
    <text class="title title-construction" x="190" y="836" font-size="99" textLength="632" lengthAdjust="spacingAndGlyphs">CONSTRUCTION</text>
    <text class="title title-material" x="190" y="924" font-size="92" textLength="410" lengthAdjust="spacingAndGlyphs">MATERIAL</text>
    <text class="title title-catalogue" x="190" y="1014" font-size="92" textLength="470" lengthAdjust="spacingAndGlyphs">CATALOGUE</text>
    <text class="title title-year" x="198" y="1214" font-size="218" textLength="462" lengthAdjust="spacingAndGlyphs">2016</text>

    <polygon class="stripe-green" points="335,1222 415,1222 385,1300 300,1300" fill="var(--stripe-green)"/>
    <polygon class="stripe-yellow" points="440,1222 535,1222 505,1300 420,1300" fill="var(--stripe-yellow)"/>
  </svg>
</main>
</body>
</html>
```